Lomira Vale Premium Full Spectrum CBD Oil

We want to launch a premium CBD oil product in several markets in Europe via an e-commerce platform. We want to create a brand that breathes quality and security. Simple design that stands out: little or no colours, original text formatting (see first three examples). Our brand is called Lomira Vale and we will launch a number of products: TORVease, TORVclear, TORVhold. We have some designs already made up but I find them too colourful, not classy enough. Is want more of a old school, black & white look, apothecary feel.... A logo is not needed to be recognizable... I add 6 designs to show what we have but this is NOT GOOD for me. You can copy the text on the label of course. PLease could you send me very clean and simple design that sticks and is very recognizable. I also add the text that should be added on the labels as the last attachment.
Target Market(s)
Europe - e-commerce: The Netherlands, Germany, France
Colors
Designer to choose only greyscale colors for use in the design.
Look and feel
Each slider illustrates characteristics of the customer's brand and the style your logo design should communicate.

```html
<!DOCTYPE html>
<html lang="en">
<head>
<meta charset="utf-8">
<title>Lomira Vale — TORVease Full Spectrum CBD Oil Label</title>
<link rel="stylesheet" href="https://fonts.googleapis.com/css2?family=Roboto+Slab:wght@800&family=Montserrat:wght@400;500&display=swap">
<style>
  :root {
    --backdrop: #ececec;
    --label-paper: #ffffff;
    --ink: #1f1f1f;
    --ink-soft: #3a3a3a;
    --label-edge: #d9d9d9;
  }
  html, body {
    margin: 0;
    padding: 0;
    width: 1200px;
    height: 1200px;
    overflow: hidden;
    background: var(--backdrop);
  }
  .canvas {
    position: relative;
    width: 1200px;
    height: 1200px;
    display: flex;
    align-items: center;
    justify-content: center;
  }
  .label {
    position: relative;
    width: 880px;
    height: 1020px;
    background: var(--label-paper);
    border: 1px solid var(--label-edge);
    box-sizing: border-box;
    display: flex;
    flex-direction: column;
    align-items: center;
    color: var(--ink);
  }
  .brand-name {
    margin-top: 215px;
    font-family: "Montserrat", sans-serif;
    font-weight: 500;
    font-size: 34px;
    letter-spacing: 0.18em;
    text-transform: uppercase;
    color: var(--ink-soft);
  }
  .product-name {
    margin: 78px 0 0;
    font-family: "Roboto Slab", serif;
    font-weight: 800;
    font-size: 168px;
    line-height: 0.88;
    letter-spacing: -0.01em;
    text-align: left;
    color: var(--ink);
  }
  .product-name span { display: block; }
  .product-type {
    margin-top: 80px;
    font-family: "Montserrat", sans-serif;
    font-weight: 400;
    font-size: 27px;
    letter-spacing: 0.04em;
    text-transform: uppercase;
    color: var(--ink-soft);
  }
  .flavour-tag {
    margin-top: 28px;
    padding: 8px 48px;
    border: 2px solid var(--ink-soft);
    font-family: "Montserrat", sans-serif;
    font-weight: 400;
    font-size: 27px;
    letter-spacing: 0.08em;
    text-transform: uppercase;
    color: var(--ink-soft);
  }
  .contents {
    margin-top: 52px;
    font-family: "Montserrat", sans-serif;
    font-weight: 400;
    font-size: 27px;
    letter-spacing: 0.06em;
    text-transform: uppercase;
    color: var(--ink-soft);
  }
</style>
</head>
<body>
  <main class="canvas">
    <section class="label">
      <div class="brand-name">Lomira Vale</div>
      <h1 class="product-name"><span>Torv</span><span>Ease</span></h1>
      <div class="product-type">Full Spectrum CBD Oil</div>
      <div class="flavour-tag">Mint Flavor</div>
      <div class="contents">30ML / 1000MG</div>
    </section>
  </main>
</body>
</html>
```